Visitenkarten-Design für Dienstleister für Musik und Feuerwerke
Zielgruppe
Meine Firma ist ein Dienstleister für Musik und Feuerwerke. Wir sind als DJ´s unterwegs und/oder als Großfeuerwerker (Pyrotechniker).
Die Zielgruppe sind Brautpaare oder Feierwillige leute. Aber genauso Firmen etc.
Aufgabenstellung
Ich bin offen für alles. Ich würde mich über ein besonderes Desgin sehr freuen, was ansprechend und besonders ist. Es soll sich von den normalen Karten abheben, sodass die Karte behalten wird, allein weil sie so schön/schick aussieht.
Facebook & Instagram name ist der selbe (talglimmer.events), und soll ruhig mit rauf.

```html
<!DOCTYPE html>
<html lang="de">
<head>
<meta charset="utf-8">
<title>Talglimmer – Visitenkarte</title>
<link rel="stylesheet" href="https://fonts.googleapis.com/css2?family=Oswald:wght@600&family=Roboto:wght@300;400;700;900&family=Roboto+Slab:wght@400&display=swap">
<style>
  :root {
    --backdrop: #d4d4d4;
    --card-white: #ffffff;
    --ink: #1a1a1a;
    --ink-soft: #3a3a3a;
    --muted: #9a9a9a;
    --accent-red: #c4173f;
    --tab-black: #0d0d0d;
    --night: #1b1718;
    --fb-blue: #4a6bb0;
  }
  * { box-sizing: border-box; margin: 0; padding: 0; }
  html, body { width: 1200px; height: 876px; overflow: hidden; }
  body {
    background: var(--backdrop);
    font-family: "Roboto", Arial, sans-serif;
    display: flex; align-items: center; justify-content: center; gap: 40px;
  }
  .card {
    width: 540px; height: 350px; position: relative; overflow: hidden;
    box-shadow: 0 10px 30px rgba(0,0,0,.25);
  }

  /* Back side: contact details */
  .card-back { background: var(--card-white); display: flex; }
  .back-photo {
    width: 215px; height: 100%; position: relative;
    background:
      radial-gradient(ellipse at 60% 30%, rgba(200,60,170,.55), transparent 45%),
      radial-gradient(ellipse at 75% 55%, rgba(80,150,170,.45), transparent 40%),
      radial-gradient(ellipse at 35% 75%, rgba(220,40,40,.8), transparent 45%),
      linear-gradient(160deg, #2a2426, #140f10);
  }
  .back-url {
    position: absolute; left: 12px; bottom: 14px;
    color: #fff; font-size: 12px; font-weight: 700; letter-spacing: .2px;
  }
  .back-info { flex: 1; position: relative; }
  .accent-bar {
    position: absolute; top: 0; left: 0; right: 40px; height: 12px;
    background: var(--accent-red);
  }
  .contact-row {
    position: absolute; right: 0; display: flex; align-items: center; gap: 14px;
  }
  .contact-text { text-align: right; color: var(--ink-soft); font-size: 14px; line-height: 1.3; }
  .contact-tab {
    width: 58px; height: 48px; background: var(--tab-black);
    border-radius: 24px 0 0 24px; display: flex; align-items: center; justify-content: center;
  }
  .contact-tab svg { width: 20px; height: 20px; fill: #fff; }
  .company-name { font-size: 26px; font-weight: 900; color: var(--ink); letter-spacing: .5px; line-height: 1.1; }
  .company-tagline { font-size: 13px; font-weight: 300; color: var(--muted); }
  .row-name { top: 34px; }
  .row-address { top: 112px; }
  .row-phone { top: 180px; }
  .row-mail { top: 244px; }
  .social {
    position: absolute; left: 22px; bottom: 16px;
    display: flex; align-items: center; gap: 8px; color: var(--ink-soft); font-size: 14px;
  }
  .social-dot { width: 16px; height: 16px; border-radius: 50%; background: var(--fb-blue); }

  /* Front side: brand */
  .card-front {
    background:
      radial-gradient(ellipse at 40% 22%, rgba(255,200,90,.55), transparent 28%),
      radial-gradient(ellipse at 25% 60%, rgba(150,90,90,.35), transparent 35%),
      linear-gradient(150deg, #2b2526, var(--night) 60%, #0e0b0c);
  }
  .brand {
    position: absolute; right: 44px; bottom: 58px; text-align: center; color: #fff;
  }
  .brand-name {
    font-family: "Oswald", "Arial Narrow", sans-serif; font-weight: 600;
    font-size: 60px; line-height: 1; letter-spacing: 1px; text-transform: uppercase;
  }
  .brand-tagline {
    font-family: "Roboto Slab", Georgia, serif; font-size: 14px;
    letter-spacing: 1px; text-transform: uppercase; margin-top: 6px;
  }
</style>
</head>
<body>

  <section class="card card-back">
    <div class="back-photo" role="img" aria-label="Foto: Feuerwerk über einer rot beleuchteten Bühne mit Publikum">
      <span class="back-url">www.talglimmer-feuerwerke.de</span>
    </div>
    <div class="back-info">
      <div class="accent-bar"></div>

      <div class="contact-row row-name">
        <div class="contact-text">
          <div class="company-name">TALGLIMMER</div>
          <div class="company-tagline">Musik &amp; Feuerwerksservice</div>
        </div>
        <div class="contact-tab">
          <svg viewBox="0 0 24 24"><circle cx="12" cy="8" r="4.5"/><path d="M3 22c0-5 4-8 9-8s9 3 9 8z"/></svg>
        </div>
      </div>

      <div class="contact-row row-address">
        <div class="contact-text">Kastanienweg 14<br>28759 Bremen</div>
        <div class="contact-tab">
          <svg viewBox="0 0 24 24"><path d="M12 2a7 7 0 0 0-7 7c0 5.5 7 13 7 13s7-7.5 7-13a7 7 0 0 0-7-7zm0 9.5A2.5 2.5 0 1 1 12 6.5a2.5 2.5 0 0 1 0 5z"/></svg>
        </div>
      </div>

      <div class="contact-row row-phone">
        <div class="contact-text">+49 170 55 23 904</div>
        <div class="contact-tab">
          <svg viewBox="0 0 24 24"><path d="M6.6 10.8a15 15 0 0 0 6.6 6.6l2.2-2.2a1 1 0 0 1 1-.25 11.4 11.4 0 0 0 3.6.57 1 1 0 0 1 1 1V20a1 1 0 0 1-1 1A17 17 0 0 1 3 4a1 1 0 0 1 1-1h3.5a1 1 0 0 1 1 1c0 1.25.2 2.45.57 3.6a1 1 0 0 1-.25 1z"/></svg>
        </div>
      </div>

      <div class="contact-row row-mail">
        <div class="contact-text">Info@talglimmer-<br>feuerwerke.de</div>
        <div class="contact-tab">
          <svg viewBox="0 0 24 24"><path d="M2 5h20v14H2z" fill="none" stroke="#fff" stroke-width="2"/><path d="M2 5l10 8 10-8" fill="none" stroke="#fff" stroke-width="2"/></svg>
        </div>
      </div>

      <div class="social">
        <span class="social-dot"></span>
        <span>@talglimmer.events</span>
      </div>
    </div>
  </section>

  <section class="card card-front" role="img" aria-label="Foto: Hand hält eine brennende Wunderkerze vor dunklem Hintergrund">
    <div class="brand">
      <div class="brand-name">Talglimmer</div>
      <div class="brand-tagline">Musik &amp; Feuerwerksservice</div>
    </div>
  </section>

</body>
</html>
```